Business Card for Quillmark Ledger - A cannabis publication for executives.

I'd like some business cards for Quillmark Ledger. The logo is done (great job!) and I need a card design I will use with PRINTLY. I made it a short project to allow time for printing before an event. These will be standard sized cards (final artwork size 3.66" x 2.16" at 300dpi) with a final card size of 3.5" x 2.0". (See PRINTLY.com if you need more info.) I might try rounded corners but am not sure yet. I think the design will work okay with rounded.

Quillmark Ledger will be a bi-weekly publication for the cannabis industry. It is targeted to investors and industry executives, not consumers or pot smokers. So our market is more B2B. However I am open to creativity and making the card something people remark on.

My contact for card:

Dana Merrow
Founder/CEO
dana@quillmarkledger.example

2740 Harlow Avenue
Boston MA 02135
(617)555-0194

Target Market(s)

Executives, Industry people and investors in the Cannabis sector.

Contact Information for Business Card

PRINTLY does do double sided and the second side can be the same or different images. Only one side is required but use of the second side would be a bonus.

Font styles to use
Serif
Sans Serif
Decorative

Colors

Designer to choose colors to be used in the design.

Requirements
Must have
• Logo, contact info
Nice to have
• Style and design to make the card stand out in a crowd.

```html
<!DOCTYPE html>
<html lang="en">
<head>
<meta charset="utf-8">
<title>Quillmark Ledger – Business Card</title>
<link rel="stylesheet" href="https://fonts.googleapis.com/css2?family=Open+Sans:wght@400;600;700&display=swap">
<style>
  :root {
    --backdrop: #1c1c1e;
    --blue-light: #2a86c8;
    --blue: #1f6fbc;
    --blue-deep: #175ea8;
    --green: #6aaa2e;
    --white: #ffffff;
    --brand-blue: #1f6fbc;
  }
  * { box-sizing: border-box; margin: 0; padding: 0; }
  html, body { width: 1200px; height: 1000px; overflow: hidden; }
  body {
    background: var(--backdrop);
    font-family: "Open Sans", Arial, sans-serif;
    position: relative;
  }
  .card {
    position: absolute;
    left: 320px;
    width: 560px;
    height: 320px;
    border-radius: 22px;
    overflow: hidden;
    background: radial-gradient(ellipse at 60% 45%, var(--blue-light) 0%, var(--blue) 55%, var(--blue-deep) 100%);
    box-shadow: 0 14px 30px rgba(0,0,0,0.55);
  }
  .card--front { top: 130px; display: flex; align-items: center; justify-content: center; }
  .card--back { top: 530px; }

  .wordmark { display: flex; align-items: center; gap: 14px; font-weight: 600; }
  .wordmark__square { width: 34px; height: 34px; }
  .card--front .wordmark { color: var(--white); font-size: 38px; }
  .card--front .wordmark__square { border: 4px solid var(--white); }

  .holder {
    position: absolute; top: 26px; left: 0; right: 0;
    text-align: center; color: var(--white);
  }
  .holder__name { font-size: 32px; font-weight: 700; letter-spacing: 0.5px; line-height: 1.1; }
  .holder__title { font-size: 16px; font-weight: 600; margin-top: 4px; }

  .brand-band {
    position: absolute; top: 118px; left: 0; right: 0; height: 104px;
    background: var(--white);
    border-top: 4px solid var(--green);
    border-bottom: 4px solid var(--green);
    display: flex; align-items: center; justify-content: center;
  }
  .brand-band .wordmark { color: var(--brand-blue); font-size: 34px; }
  .brand-band .wordmark__square { border: 4px solid var(--brand-blue); }

  .contact {
    position: absolute; left: 30px; bottom: 18px;
    list-style: none; color: var(--white); font-size: 13px; line-height: 1.45;
  }
  .contact li { display: flex; align-items: center; gap: 9px; }
  .contact svg { width: 11px; height: 11px; fill: var(--white); flex: none; }

  .address {
    position: absolute; right: 30px; top: 238px;
    color: var(--white); font-size: 13px; text-align: right; line-height: 1.35; font-style: normal;
  }
</style>
</head>
<body>
  <section class="card card--front" aria-label="Card front">
    <div class="wordmark"><span class="wordmark__square"></span>Quillmark Ledger</div>
  </section>

  <section class="card card--back" aria-label="Card back">
    <div class="holder">
      <p class="holder__name">DANA MERROW</p>
      <p class="holder__title">Founder/CEO</p>
    </div>
    <div class="brand-band">
      <div class="wordmark"><span class="wordmark__square"></span>Quillmark Ledger</div>
    </div>
    <address class="address">2740 Harlow Avenue<br>Boston MA 02135</address>
    <ul class="contact">
      <li><svg viewBox="0 0 24 24" aria-hidden="true"><path d="M6.6 10.8a15.1 15.1 0 0 0 6.6 6.6l2.2-2.2c.3-.3.7-.4 1-.2 1.1.4 2.3.6 3.6.6.6 0 1 .4 1 1V20c0 .6-.4 1-1 1C10.6 21 3 13.4 3 4c0-.6.4-1 1-1h3.5c.6 0 1 .4 1 1 0 1.3.2 2.5.6 3.6.1.3 0 .7-.2 1z"/></svg>617 555 0194</li>
      <li><svg viewBox="0 0 24 24" aria-hidden="true"><path d="M2 5h20v14H2z M2 5l10 8 10-8" fill="none" stroke="#fff" stroke-width="2.5"/></svg>dana@quillmarkledger.example</li>
      <li><svg viewBox="0 0 24 24" aria-hidden="true"><circle cx="13" cy="10" r="7" fill="none" stroke="#fff" stroke-width="2.5"/><path d="M8 15l-6 6" stroke="#fff" stroke-width="2.5"/></svg>www.quillmarkledger.example</li>
    </ul>
  </section>
</body>
</html>
```